Marbella Specialty Coffee needs a Packaging design

We need packaging design for coffee that suits our brand identity, that is the best quality in Mexico.
We only sell mexican coffee with Q scores above 80
We are evaluating 3 types of packaging: Bag, Box and Cillinder can
The specific package format will be decided based on the designs that we get.

Target Market(s)

Coffee experts and enthusiast.
People that relate the Coffee consumption and experience with wine tasting and Bon Vivant way

Requirements
Should not have
• Photos any mexican cliché

```html
<!DOCTYPE html>
<html lang="en">
<head>
<meta charset="utf-8">
<title>Marbella Specialty Coffee – Dark Roast Label</title>
<link rel="stylesheet" href="https://fonts.googleapis.com/css2?family=Lato:wght@400;700&family=Tinos&display=swap">
<style>
  :root {
    --cream: #e7d9c5;
    --olive: #9a8751;
    --tan: #d4b38d;
    --brown: #8a4829;
    --espresso: #5c2916;
    --ink: #7a3b22;
    --type-light: #ead5b8;
    --type-muted: #c8a985;
  }
  * { margin: 0; padding: 0; box-sizing: border-box; }
  html, body { width: 1200px; height: 498px; overflow: hidden; background: var(--cream); }
  .label {
    position: relative;
    width: 1200px;
    height: 498px;
    overflow: hidden;
    font-family: "Lato", sans-serif;
  }
  .band { position: absolute; left: 0; width: 100%; }
  .band--cream { top: 0; height: 100px; background: var(--cream); }
  .band--olive { top: 100px; height: 95px; background: var(--olive); }
  .band--tan { top: 195px; height: 105px; background: var(--tan); }
  .band--brown { top: 300px; height: 100px; background: var(--brown); }
  .band--espresso { top: 400px; height: 98px; background: var(--espresso); }

  .brand {
    position: absolute;
    left: 380px;
    top: 120px;
    display: flex;
    align-items: center;
    gap: 34px;
  }
  .brand__mark { width: 150px; height: 150px; flex: none; }
  .brand__name {
    color: var(--ink);
    font-family: "Lato", sans-serif;
    font-weight: 400;
    line-height: 1;
  }
  .brand__name-main { display: block; font-size: 82px; letter-spacing: 1px; }
  .brand__name-sub { display: block; font-size: 31px; margin-top: 14px; padding-left: 22px; }

  .variety {
    position: absolute;
    font-family: "Lato", sans-serif;
    font-weight: 700;
    letter-spacing: 2px;
    line-height: 1;
  }
  .variety--dark { left: 445px; top: 347px; font-size: 54px; color: var(--type-light); }
  .variety--roast { left: 554px; top: 397px; font-size: 54px; color: var(--type-muted); }

  .net-weight {
    position: absolute;
    left: 578px;
    top: 458px;
    font-family: "Tinos", serif;
    font-size: 19px;
    letter-spacing: 2px;
    color: var(--type-light);
  }
</style>
</head>
<body>
  <main class="label">
    <div class="band band--cream"></div>
    <div class="band band--olive"></div>
    <div class="band band--tan"></div>
    <div class="band band--brown"></div>
    <div class="band band--espresso"></div>

    <div class="brand">
      <svg class="brand__mark" viewBox="0 0 150 150" aria-hidden="true">
        <circle cx="75" cy="75" r="70" fill="var(--ink)"/>
      </svg>
      <p class="brand__name">
        <span class="brand__name-main">Marbella</span>
        <span class="brand__name-sub">Specialty Coffee</span>
      </p>
    </div>

    <p class="variety variety--dark">DARK</p>
    <p class="variety variety--roast">ROAST</p>
    <p class="net-weight">12 oz.</p>
  </main>
</body>
</html>
```